MS word document templates for consultancy

I need the following templates for my business using my logo as branding.

- General report template
- Letter head template
- Tender proposal template

The templates should be sleek and with minimal colors, but with a small amount of green and grey where appropriate (as per attached logo and email signature). Font should be consistent with the text in the email signature.

```html
<!DOCTYPE html>
<html lang="en">
<head>
<meta charset="utf-8">
<title>Northvale Group – Letterhead</title>
<link href="https://fonts.googleapis.com/css2?family=Arimo:wght@400;700&display=swap" rel="stylesheet">
<style>
  :root {
    --green: #2a9446;
    --ink: #111111;
    --paper: #ffffff;
    --band-light: #fafafa;
  }
  * { margin: 0; padding: 0; box-sizing: border-box; }
  html, body { width: 848px; height: 1200px; overflow: hidden; background: var(--paper); }
  body { font-family: 'Arimo', Arial, sans-serif; color: var(--ink); }
  .letterhead { position: relative; width: 848px; height: 1200px; overflow: hidden; background: var(--paper); }
  .corner-art { position: absolute; top: 0; left: 0; width: 848px; height: 200px; }
  .brand-name {
    position: absolute; left: 84px; top: 182px;
    font-size: 40px; font-weight: 400; color: var(--ink); letter-spacing: 0.5px; line-height: 1;
  }
  .sender { position: absolute; right: 86px; top: 191px; text-align: right; }
  .sender-name { font-size: 21px; font-weight: 700; color: var(--green); line-height: 30px; }
  .sender-role { font-size: 21px; font-weight: 400; color: var(--ink); line-height: 30px; }
  .contact-bar { position: absolute; top: 1079px; left: 84px; display: flex; align-items: center; }
  .contact-item { display: flex; align-items: center; font-size: 17px; }
  .contact-item svg { width: 28px; height: 28px; margin-right: 16px; }
  .contact-phone { width: 196px; }
  .contact-email { width: 248px; }
  .bottom-band { position: absolute; left: 0; bottom: 0; width: 848px; height: 17px; background: var(--green); }
</style>
</head>
<body>
<main class="letterhead">
  <svg class="corner-art" viewBox="0 0 848 200" aria-hidden="true">
    <path d="M0 0 H414 Q200 50 0 177 Z" fill="var(--ink)"/>
    <path d="M0 0 H192 Q90 40 0 93 Z" fill="var(--band-light)"/>
    <path d="M0 0 H54 Q25 10 0 23 Z" fill="var(--green)"/>
    <path d="M654 0 Q760 38 848 94 V0 Z" fill="var(--green)"/>
  </svg>

  <div class="brand-name">Northvale Group</div>

  <div class="sender">
    <p class="sender-name">Daniel Reeve</p>
    <p class="sender-role">Managing Director</p>
  </div>

  <div class="contact-bar">
    <div class="contact-item contact-phone">
      <svg viewBox="0 0 28 28" aria-hidden="true">
        <circle cx="14" cy="14" r="12.5" fill="none" stroke="var(--green)" stroke-width="1.6"/>
        <path d="M10 7.5 l2.2 3.2 -1.3 1.4 q1 3.2 4.2 5 l1.4 -1.3 3.2 2.2 -1.6 2.3 q-5.5 -0.6 -9.6 -7.3 q-1 -2.6 -0.4 -4.2 Z" fill="var(--green)"/>
      </svg>
      <span>0400 555 019</span>
    </div>
    <div class="contact-item contact-email">
      <svg viewBox="0 0 28 28" aria-hidden="true">
        <circle cx="14" cy="14" r="13.5" fill="var(--green)"/>
        <rect x="8.5" y="10" width="11" height="8" rx="1" fill="var(--paper)"/>
        <path d="M8.8 10.5 L14 14.6 L19.2 10.5" fill="none" stroke="var(--green)" stroke-width="1.3"/>
      </svg>
      <span>hello@youremail.com</span>
    </div>
    <div class="contact-item contact-web">
      <svg viewBox="0 0 28 28" aria-hidden="true">
        <circle cx="14" cy="14" r="13.5" fill="var(--green)"/>
        <g fill="none" stroke="var(--paper)" stroke-width="1.3">
          <ellipse cx="14" cy="14" rx="5" ry="13.5"/>
          <line x1="14" y1="0.5" x2="14" y2="27.5"/>
          <line x1="0.5" y1="10" x2="27.5" y2="10"/>
          <line x1="0.5" y1="18" x2="27.5" y2="18"/>
        </g>
      </svg>
      <span>www.yourwebsite.com</span>
    </div>
  </div>

  <div class="bottom-band"></div>
</main>
</body>
</html>
```